Marlow Realty Real Estate Brokerage Recruiting Flyer

We are a real estate brokerage looking to hire more real estate agents. We need to list everything we have to offer as a company so real estate agents will join our company. this is our company website: www.Marlowrealty.example .

100% COMMISSION NO MONTHLY FEE
$450 Flat Transaction FEE

What We Offer:
24/7 Office Access
Free E & O Insurance for 1st Year
Free Online CE and PLE
Free 1,000 Business Cards
Free Professional Social Media Marketing
Free Printing, Scanning, and Copies
Free Buyer and Seller Presentation Packages
Free Filquay Cloud Based Document Management Access
Access to our Internal Brokerage Forum
Company Profit Sharing!
Private Offices Available to Rent

*Lead Generation Software with over 3,000 Leads
*10 Leads to Start
* Free Personal CRM and Website
*Restrictions and Rules apply

Company Address:
4817 Amberfield Road
Suite 512
Fairfax, VA 22194
Phone: 703-555-0147
email: info@marlowrealty.example

Target Market(s)

Real Estate Agents

Industry/Entity Type

Real Estate

Colors
0555a3
ffffff

Requirements
Must have
• 100% COMMISSION NO MONTHLY FEE
$450 Flat Transaction FEE

What We Offer:
24/7 Office Access
Free Online CE and PLE
Free 1,000 Business Cards
Company Profit Sharing!

*10 Leads to Start

Company Address:
4817 Amberfield Road
Suite 512
Fairfax, VA 22194
Phone: 703-555-0147

```html
<!DOCTYPE html>
<html lang="en">
<head>
<meta charset="utf-8">
<title>Marlow Realty – Join Our Team</title>
<link rel="stylesheet" href="https://fonts.googleapis.com/css2?family=Jost:wght@300;400;500;600;700&family=Oswald:wght@600;700&display=swap">
<style>
  :root {
    --navy: #213a6f;
    --navy-dark: #1a2f5c;
    --white: #ffffff;
    --ink: #1d1d1f;
    --band: #d6d6d8;
    --stage: #7a7a7a;
    --photo-warm: #e8cfae;
    --photo-light: #f6ece0;
  }
  * { box-sizing: border-box; margin: 0; padding: 0; }
  html, body { width: 1200px; height: 2400px; overflow: hidden; }
  body { background: var(--stage); font-family: "Jost", sans-serif; color: var(--ink); position: relative; }

  .flyer { position: absolute; left: 0; top: 424px; width: 1200px; height: 1552px; background: var(--white); overflow: hidden; }
  .flyer > * { position: absolute; }

  .brand { left: 52px; top: 90px; display: flex; align-items: center; gap: 22px; }
  .brand-mark { width: 58px; height: 58px; background: var(--navy); }
  .brand-name { font-size: 72px; font-weight: 500; color: var(--navy); letter-spacing: 2px; line-height: 1; }

  .call { left: 739px; top: 76px; }
  .call-label { font-size: 30px; font-weight: 600; color: var(--navy); letter-spacing: .5px; }
  .call-number { font-family: "Oswald", sans-serif; font-weight: 700; font-size: 78px; line-height: 1; color: var(--navy); margin-top: 4px; letter-spacing: 1px; }

  .hero-photo { left: 0; top: 270px; width: 1200px; height: 549px;
    background: linear-gradient(100deg, var(--photo-light) 0%, var(--photo-warm) 55%, #d9b58c 100%); }

  .offer-panel { left: 38px; top: 267px; width: 441px; height: 947px; background: var(--navy); color: var(--white); text-align: center; }
  .panel-join { font-size: 124px; font-weight: 300; line-height: 1; margin-top: 70px; letter-spacing: 2px; }
  .panel-team { font-size: 58px; font-weight: 700; line-height: 1; margin-top: 10px; }
  .panel-rule { width: 350px; margin: 32px auto 0; border-top: 3px dotted rgba(255,255,255,.8); }
  .panel-big { font-family: "Oswald", sans-serif; font-weight: 600; font-size: 70px; line-height: 1; margin-top: 30px; }
  .panel-sub { font-size: 23px; font-weight: 500; line-height: 1.3; margin-top: 8px; }
  .panel-perks { list-style: none; text-align: left; margin: 62px 0 0 52px; }
  .panel-perks li { display: flex; gap: 14px; font-size: 20px; font-weight: 400; line-height: 1.2; margin-bottom: 24px; }
  .perk-icon { flex: none; width: 22px; height: 18px; margin-top: 3px; }

  .license { left: 30px; top: 1256px; width: 455px; height: 101px; border: 2px dashed var(--navy); border-radius: 22px; text-align: center; padding-top: 14px; }
  .license-label { font-size: 24px; font-weight: 300; color: var(--navy); line-height: 1.1; }
  .license-states { font-size: 24px; font-weight: 600; line-height: 1.2; }

  .offers-title { left: 479px; width: 721px; top: 838px; text-align: center; font-size: 30px; font-weight: 600; color: var(--navy); letter-spacing: 14px; }
  .offer { display: flex; align-items: center; gap: 12px; font-size: 20px; line-height: 1.2; font-weight: 400; }
  .offer-icon { flex: none; width: 44px; height: 44px; }
  .col-left { left: 540px; }
  .col-right { left: 908px; }

  .footer { left: 0; top: 1397px; width: 1200px; height: 155px; background: var(--band); display: flex; align-items: center; }
  .footer-cell { text-align: center; font-size: 22px; line-height: 1.25; position: relative; height: 100px; display: flex; flex-direction: column; justify-content: center; }
  .footer-cell + .footer-cell { border-left: 2px solid var(--navy); }
  .footer-label { font-weight: 300; }
  .footer-value { font-weight: 600; }
</style>
</head>
<body>
<main class="flyer">
  <header class="brand">
    <span class="brand-mark"></span>
    <span class="brand-name">Marlow Realty</span>
  </header>

  <div class="call">
    <p class="call-label">CALL US TODAY!</p>
    <p class="call-number">703-555-0147</p>
  </div>

  <div class="hero-photo" role="img" aria-label="Smiling family sitting under a white cardboard roof shape in a bright wooden room"></div>

  <section class="offer-panel">
    <h1 class="panel-join">JOIN</h1>
    <p class="panel-team">OUR TEAM!</p>
    <div class="panel-rule"></div>
    <p class="panel-big">100%</p>
    <p class="panel-sub">COMMISSION<br>NO MONTHLY FEE</p>
    <div class="panel-rule"></div>
    <p class="panel-big">$450</p>
    <p class="panel-sub">FLAT TRANSACTION FEE</p>
    <ul class="panel-perks">
      <li><svg class="perk-icon" viewBox="0 0 22 18"><path d="M1 17h20M3 16V8h3v8M9 16V3h3v13M15 16V6h3v10" fill="none" stroke="#fff" stroke-width="2"/></svg><span>Lead Generation Software with<br>over 3,000 Leads</span></li>
      <li><svg class="perk-icon" viewBox="0 0 22 18"><path d="M1 17h20M3 16V8h3v8M9 16V3h3v13M15 16V6h3v10" fill="none" stroke="#fff" stroke-width="2"/></svg><span>10 Leads to Start</span></li>
      <li><svg class="perk-icon" viewBox="0 0 22 18"><path d="M1 17h20M3 16V8h3v8M9 16V3h3v13M15 16V6h3v10" fill="none" stroke="#fff" stroke-width="2"/></svg><span>Free Personal CRM and Website</span></li>
      <li><svg class="perk-icon" viewBox="0 0 22 18"><path d="M1 17h20M3 16V8h3v8M9 16V3h3v13M15 16V6h3v10" fill="none" stroke="#fff" stroke-width="2"/></svg><span>Restrictions and Rules apply</span></li>
    </ul>
  </section>

  <div class="license">
    <p class="license-label">LISENCED</p>
    <p class="license-states">DC, Maryland, Virginia &amp; Indiana</p>
  </div>

  <h2 class="offers-title">WHAT WE OFFER</h2>

  <div class="offer col-left" style="top:906px"><svg class="offer-icon" viewBox="0 0 44 44"><circle cx="22" cy="22" r="20" fill="none" stroke="#213a6f" stroke-width="2.5"/><rect x="13" y="13" width="18" height="17" rx="2" fill="none" stroke="#213a6f" stroke-width="2.5"/><circle cx="22" cy="23" r="4" fill="none" stroke="#213a6f" stroke-width="2"/></svg><span>24/7<br>Office Access</span></div>
  <div class="offer col-left" style="top:976px"><svg class="offer-icon" viewBox="0 0 44 44"><circle cx="22" cy="22" r="20" fill="none" stroke="#213a6f" stroke-width="2.5"/><path d="M11 22a11 9 0 0 1 22 0zM22 22v8a3 3 0 0 1-5 1" fill="#213a6f" stroke="#213a6f" stroke-width="2"/></svg><span>Free E &amp; O Insurance<br>for 1st Year</span></div>
  <div class="offer col-left" style="top:1046px"><svg class="offer-icon" viewBox="0 0 44 44"><circle cx="22" cy="22" r="20" fill="none" stroke="#213a6f" stroke-width="2.5"/><rect x="12" y="13" width="20" height="14" fill="none" stroke="#213a6f" stroke-width="2.5"/><path d="M17 32h10M22 27v5" stroke="#213a6f" stroke-width="2.5"/></svg><span>Free Online<br>CE and PLE</span></div>
  <div class="offer col-left" style="top:1116px"><svg class="offer-icon" viewBox="0 0 44 44"><circle cx="22" cy="22" r="20" fill="none" stroke="#213a6f" stroke-width="2.5"/><rect x="11" y="14" width="22" height="16" rx="1" fill="none" stroke="#213a6f" stroke-width="2.5"/><rect x="14" y="18" width="6" height="6" fill="#213a6f"/><path d="M23 19h7M23 23h7M14 27h16" stroke="#213a6f" stroke-width="2"/></svg><span>Free 1,000<br>Business Cards</span></div>
  <div class="offer col-left" style="top:1190px"><svg class="offer-icon" viewBox="0 0 44 44"><circle cx="22" cy="22" r="20" fill="none" stroke="#213a6f" stroke-width="2.5"/><path d="M15 15l14 14M29 15L15 29" stroke="#213a6f" stroke-width="2.5"/><circle cx="22" cy="22" r="3.5" fill="#213a6f"/><circle cx="15" cy="15" r="3" fill="#213a6f"/><circle cx="29" cy="15" r="3" fill="#213a6f"/><circle cx="15" cy="29" r="3" fill="#213a6f"/><circle cx="29" cy="29" r="3" fill="#213a6f"/></svg><span>Free Professional<br>Social Media<br>Marketing</span></div>
  <div class="offer col-left" style="top:1284px"><svg class="offer-icon" viewBox="0 0 44 44"><circle cx="22" cy="22" r="20" fill="none" stroke="#213a6f" stroke-width="2.5"/><rect x="16" y="12" width="12" height="7" fill="none" stroke="#213a6f" stroke-width="2"/><rect x="12" y="19" width="20" height="9" rx="2" fill="#213a6f"/><rect x="16" y="25" width="12" height="7" fill="#fff" stroke="#213a6f" stroke-width="2"/></svg><span>Free Printing,<br>Scanning,and Copies</span></div>

  <div class="offer col-right" style="top:926px"><svg class="offer-icon" viewBox="0 0 44 44"><circle cx="22" cy="22" r="20" fill="none" stroke="#213a6f" stroke-width="2.5"/><rect x="11" y="12" width="22" height="15" fill="#213a6f"/><path d="M22 27v6M16 33h12" stroke="#213a6f" stroke-width="2.5"/><path d="M15 23l5-5 3 3 5-5" stroke="#fff" stroke-width="2" fill="none"/></svg><span>Free Buyer and<br>Seller Presentation<br>Packages</span></div>
  <div class="offer col-right" style="top:1020px"><svg class="offer-icon" viewBox="0 0 44 44"><circle cx="22" cy="22" r="20" fill="none" stroke="#213a6f" stroke-width="2.5"/><path d="M13 24a5 5 0 0 1 3-9 7 7 0 0 1 13 1 4 4 0 0 1 1 8z" fill="#213a6f"/><path d="M16 26v5M22 26v6M28 26v5" stroke="#213a6f" stroke-width="2"/></svg><span>Free Filquay Cloud<br>Based Document<br>Management Access</span></div>
  <div class="offer col-right" style="top:1114px"><svg class="offer-icon" viewBox="0 0 44 44"><circle cx="22" cy="22" r="20" fill="none" stroke="#213a6f" stroke-width="2.5"/><circle cx="22" cy="22" r="10" fill="none" stroke="#213a6f" stroke-width="2.5"/><path d="M12 22h20M22 12c-5 6-5 14 0 20M22 12c5 6 5 14 0 20" fill="none" stroke="#213a6f" stroke-width="1.8"/></svg><span>Access to our Internal<br>Brokerage Forum</span></div>
  <div class="offer col-right" style="top:1184px"><svg class="offer-icon" viewBox="0 0 44 44"><circle cx="22" cy="22" r="20" fill="none" stroke="#213a6f" stroke-width="2.5"/><circle cx="24" cy="17" r="6" fill="none" stroke="#213a6f" stroke-width="2.2"/><path d="M10 29l5-2h7l6-3 3 2-9 6h-12z" fill="#213a6f"/></svg><span>Company<br>Profit Sharing!</span></div>
  <div class="offer col-right" style="top:1254px"><svg class="offer-icon" viewBox="0 0 44 44"><circle cx="22" cy="22" r="20" fill="none" stroke="#213a6f" stroke-width="2.5"/><rect x="13" y="18" width="9" height="14" fill="#213a6f"/><rect x="22" y="22" width="8" height="10" fill="none" stroke="#213a6f" stroke-width="2"/><circle cx="28" cy="14" r="3.5" fill="none" stroke="#213a6f" stroke-width="2"/></svg><span>Private Offices<br>Available to Rent</span></div>

  <footer class="footer">
    <div class="footer-cell" style="width:354px"><span class="footer-label">OFFICE ADDRESS</span><span class="footer-value">4817 Amberfield Road</span><span class="footer-value">Suite 512</span></div>
    <div class="footer-cell" style="width:220px"><span class="footer-label">FAIRFAX</span><span class="footer-value">VA 22194</span></div>
    <div class="footer-cell" style="width:323px"><span class="footer-label">EMAIL</span><span class="footer-value">info@marlowrealty.example</span></div>
    <div class="footer-cell" style="width:303px"><span class="footer-label">VISIT US</span><span class="footer-value">www.Marlowrealty.example</span></div>
  </footer>
</main>
</body>
</html>
```